GUARANTEED 4 sample word cards for inclusive primary education (the swan, the icebear, the cat, sad)

in short: it's about drawing a swan, at icebear, a cat, a sad person (male / female) and arranging them on word cards with some additional information As there which only one design submitted, Which was missing the point I Decided to translate everything myself and upload it again. Requirements Within an open educational ressources (OER) project, materials for the interest-based spelling workout are to be created. In the preparation of this project four example sample word cards are to be developed. Later They Should be compiled dynamically from a database. Since the needs of the teachers are very different, it would be advantageous to integrate the different design elements as layers in Photoshop so did one can show how diverse the cards can look later by hiding / showing the layers. The materials shoulderstand be distributed under cc-0 license. It is about 4 sample cards (the swan, the icebear, the cat, sad), Which shoulderstand demonstrate how search cards can look. German: As part of an OER project are materials to interest-based spelling learning occur. In the preparation of the project (to be created also a permanent position for a / n Designer / -in under which) are four examplarische Sample word cards are developed. Later this should be assembled dynamically from a database. Since the needs of teachers / -Innen are very different, it would be desirable to integrate the various design elements as layers in Photoshop, so you can show how diverse can look the cards later. The materials are to be distributed under cc-0 license. It is about 4 example cards that demonstrate how can such cards look. The most expensive part is undoubtedly the drawings (polar bear, swan, cat and sad child / sad person). Common elements - speech symbol Veldarini (see http: //media.lirobeck-press. example / media / catalog / product / cache / 4 / image / 3ab51cde90417f62c8e0a4d19253b78a / 0/7 / 04189_1.jpg) - underline articles colored or colored or point mark (male - red, male - blue, neuter - green) - writing of definition and article (once https://glyphshelf.example/en/font/grundschrift and once a school Ausgangsschrift eg https://www.tomvaro.example/hub/Lumen/de_DE.CMS.displayCMS.318406./die-schulausgangsschrift -sas-free-download-tomvaro) - Ruling based on http://www.b-straleck.example/wp-content/uploads/2010/01/Heft-006-innen.png (and even without house) - picture on the right side - pictures with people, each as a girl / boy, different skin colors (or all as layers in Photoshop, where I can hide it myself) - syllable sheets (instead of the | http://trymindquill.example/wp- content / uploads / 2015_2_Silbenboegen_Kombo.png) - colored syllables (blue and red) - stem color (red), ending black - cases if necessary on the back of the card - Format Din A7, rounded corners images should as svg / or levels exist (different skin color / hair color / gender) drawings should stylized and not be too childish and love of detail, so that they are attractive to adults (and as can be used in work with fugitives). You should also black / white and be usable with red / green blindness. The exact requirements are in the description file. For any questions please contact via the platform or haraldp.ostwig@hs-varnholt.example Ps: If a logo for (spelling) learning, including drops, it is also nich bad;) If you interested in a long-term employment in a project have the university, we appreciate if you mention this.
pupils in primary school, so but older students and adults (for example refugees who started to learn the language) students / -Innen primary school (until fourth grade) as well as older adolescents / adults, therefore, not to child pictures
Education
- see additional file

- psd files with levels, to show and hide different elements self drawn images, Which Could be released under a CC-0 license. see additional file for more info and sample German: .psd files with labeled layers, in which the individual elements can be hidden. Self-drawn graphics which can then be released under cc-0 Stock

```html
<!DOCTYPE html>
<html lang="de">
<head>
<meta charset="utf-8">
<title>Wortkarte – der Schwan</title>
<link href="https://fonts.googleapis.com/css2?family=Source+Sans+3:wght@400;600;700&display=swap" rel="stylesheet">
<style>
  :root {
    --page-bg: #e6e6e6;
    --front-top: #e9f7fd;
    --front-bottom: #a9dbf3;
    --back-top: #f7f7fc;
    --back-bottom: #d9dbf0;
    --ink: #1a1a1a;
    --article-blue: #0a2fa0;
    --tag-blue: #062f9e;
    --case-blue: #2e8fe8;
    --gender-red: #e81010;
    --rule: #4a4a4a;
    --rule-light: #8a8a8a;
  }
  * { margin: 0; padding: 0; box-sizing: border-box; }
  html, body { width: 1200px; height: 1000px; overflow: hidden; }
  body {
    position: relative;
    background: var(--page-bg);
    font-family: "Source Sans 3", sans-serif;
    color: var(--ink);
  }
  .card {
    position: absolute;
    width: 676px;
    height: 476px;
    border-radius: 12px;
    overflow: hidden;
  }
  .card--front {
    left: 30px; top: 22px;
    background: radial-gradient(circle at 35% 30%, var(--front-top) 0%, #cdebf8 55%, var(--front-bottom) 100%);
  }
  .card--back {
    left: 430px; top: 508px;
    background: radial-gradient(circle at 40% 60%, var(--back-top) 0%, #eceef8 55%, var(--back-bottom) 100%);
  }
  .gender-mark {
    position: absolute; left: 24px; top: 24px; width: 38px; height: 38px;
    border-radius: 50%;
    background: var(--gender-red);
  }
  .word-article, .word-noun, .word-plural-article, .example-sentence, .nomen-label {
    position: absolute; line-height: 1; white-space: nowrap;
  }
  .word-article { left: 76px; top: 25px; font-size: 38px; font-weight: 700; color: var(--article-blue); }
  .word-noun { left: 78px; top: 62px; font-size: 58px; font-weight: 400; }
  .word-plural-article { left: 78px; top: 129px; font-size: 40px; font-weight: 700; }
  .word-picture {
    position: absolute; left: 526px; top: 19px; width: 130px; height: 189px;
    border-radius: 40px 40px 60px 60px;
    background: linear-gradient(160deg, #ffffff 0%, #eef1f4 70%, #d9dde2 100%);
  }
  .example-sentence { left: 76px; top: 298px; font-size: 34px; font-weight: 400; color: #2a2a2a; }
  .tag-bar {
    position: absolute; left: 78px; top: 407px; width: 408px; height: 49px;
    background: var(--tag-blue); border-radius: 3px;
    display: flex; align-items: center; justify-content: space-between;
    padding: 0 11px 0 13px;
    color: #fff; font-size: 27px; font-weight: 700;
  }
  .tag-bar .sep { font-weight: 400; }
  .word-class-mark { position: absolute; left: 503px; top: 408px; width: 49px; height: 41px; }
  .nomen-label { left: 561px; top: 427px; font-size: 27px; font-weight: 700; color: #222; }

  .case-table { position: absolute; left: 0; top: 0; width: 100%; height: 100%; }
  .rule { position: absolute; height: 1px; background: var(--rule-light); }
  .rule--strong { height: 2px; background: var(--rule); }
  .cell { position: absolute; line-height: 1; font-size: 19px; white-space: nowrap; }
  .cell--head { font-weight: 700; letter-spacing: 0.3px; color: #333; }
  .cell--case { font-weight: 700; color: var(--case-blue); font-size: 20px; }
  .cell--form { color: #333; font-size: 20px; }
</style>
</head>
<body>

<section class="card card--front">
  <div class="gender-mark" role="img" aria-label="Genusmarke maskulin"></div>
  <div class="word-article">der</div>
  <div class="word-noun">Schwan</div>
  <div class="word-plural-article">die</div>
  <div class="word-picture" role="img" aria-label="Zeichnung eines weißen Schwans mit orangem Schnabel"></div>
  <p class="example-sentence">Der Schwan fliegt über den See.</p>
  <div class="tag-bar">
    <span>Tier</span><span class="sep">|</span><span>groß</span><span class="sep">|</span><span>weiß</span><span class="sep">|</span><span>Vogel</span>
  </div>
  <svg class="word-class-mark" viewBox="0 0 49 41" aria-hidden="true">
    <polygon points="24.5,0 49,41 0,41" fill="#000"/>
  </svg>
  <div class="nomen-label">Nomen</div>
</section>

<section class="card card--back">
  <div class="case-table">
    <div class="rule" style="left:266px; width:388px; top:114px;"></div>
    <div class="cell cell--head" style="left:274px; top:129px;">SINGULAR</div>
    <div class="cell cell--head" style="left:514px; top:129px;">PLURAL</div>
    <div class="rule rule--strong" style="left:18px; width:636px; top:153px;"></div>

    <div class="cell cell--case" style="left:33px; top:171px;">Nominativ (wer?/was?)</div>
    <div class="cell cell--form" style="left:274px; top:171px;">der Schwan</div>
    <div class="cell cell--form" style="left:514px; top:171px;">die Schwäne</div>
    <div class="rule" style="left:18px; width:636px; top:210px;"></div>

    <div class="cell cell--case" style="left:33px; top:228px;">Genitiv (wessen?)</div>
    <div class="cell cell--form" style="left:274px; top:228px;">des Schwanes, Schwans</div>
    <div class="cell cell--form" style="left:514px; top:228px;">der Schwäne</div>
    <div class="rule" style="left:18px; width:636px; top:267px;"></div>

    <div class="cell cell--case" style="left:33px; top:285px;">Dativ (wem?)</div>
    <div class="cell cell--form" style="left:274px; top:285px;">dem Schwan</div>
    <div class="cell cell--form" style="left:514px; top:285px;">den Schwänen</div>
    <div class="rule" style="left:18px; width:636px; top:325px;"></div>

    <div class="cell cell--case" style="left:33px; top:342px;">Akkusativ (wen?/was?)</div>
    <div class="cell cell--form" style="left:274px; top:342px;">den Schwan</div>
    <div class="cell cell--form" style="left:514px; top:342px;">die Schwäne</div>
    <div class="rule" style="left:18px; width:636px; top:374px;"></div>
  </div>
</section>

</body>
</html>
```